need a clean, modern job advertisement designed for social media (Facebook & Instagram).

The post is to advertise two positions:
• Leading Hand Boilermaker
• Dragline Fitter
We want the design to match our KRT Plant Services branding: blue, white, strong, professional, mining-industry style.
What the design should include:
Bold headline: “WE’RE HIRING”
Sub-headline: “Leading Hand Boilermaker & Dragline Fitter”
Key points:
• Bowen Basin based
• Dragline & shovel maintenance
• Great pay + long-term work
• Locally owned & operated
KRT logo placed cleanly
Space for 1–2 images (boilermaking or dragline work)
Design style:
Strong and industrial
Blue/white colour scheme
Easy to read at a glance
Suitable for a square 1080×1080 design

```html
<!DOCTYPE html>
<html lang="en">
<head>
<meta charset="UTF-8">
<title>KRT Plant Services – We're Hiring</title>
<link rel="stylesheet" href="https://fonts.googleapis.com/css2?family=Montserrat:wght@800;900&family=Roboto+Condensed:wght@700&display=swap">
<style>
  :root {
    --brand-blue: #1a9be0;
    --white: #ffffff;
    --ink: #1c1d22;
    --photo-dark: #15151b;
    --photo-mid: #2a2a33;
    --spark: #e89a3c;
  }
  * { margin: 0; padding: 0; box-sizing: border-box; }
  html, body { width: 1200px; height: 1200px; overflow: hidden; background: var(--photo-dark); }
  .poster {
    position: relative;
    width: 1200px;
    height: 1200px;
    overflow: hidden;
    font-family: "Roboto Condensed", "Arial Narrow", sans-serif;
    color: var(--white);
  }
  .hero-photo {
    position: absolute; inset: 0;
    background:
      radial-gradient(ellipse 420px 300px at 800px 1010px, rgba(232,154,60,0.75), rgba(232,154,60,0) 70%),
      radial-gradient(ellipse 300px 260px at 230px 330px, rgba(140,150,175,0.45), rgba(140,150,175,0) 75%),
      linear-gradient(160deg, var(--photo-mid) 0%, var(--photo-dark) 55%, #241a16 100%);
  }
  .top-rule {
    position: absolute; left: 72px; top: 0; width: 1083px; height: 13px;
    background: var(--brand-blue);
  }
  .logo-tag {
    position: absolute; left: 728px; top: 13px; width: 428px; height: 400px;
  }
  .logo-tag svg { position: absolute; inset: 0; }
  .logo-name {
    position: absolute; left: 0; top: 0; width: 428px; height: 360px;
    display: flex; align-items: center; justify-content: center; gap: 16px;
    font-family: "Montserrat", sans-serif; font-weight: 800; font-size: 40px;
    color: var(--brand-blue); text-align: left; line-height: 1.05;
  }
  .logo-name .mark { width: 38px; height: 38px; background: var(--brand-blue); flex: none; }
  .key-points {
    position: absolute; right: 539px; top: 58px;
    list-style: none; text-align: right;
    font-size: 37px; line-height: 52px;
  }
  .key-points li::before { content: "· "; }
  .headline-small {
    position: absolute; left: 283px; top: 432px;
    font-family: "Montserrat", sans-serif; font-weight: 900; font-size: 94px; line-height: 1;
    letter-spacing: -1px;
  }
  .mask-icon { position: absolute; left: 640px; top: 436px; width: 46px; height: 76px; }
  .headline-big {
    position: absolute; left: 176px; top: 510px; width: 940px;
    font-family: "Montserrat", sans-serif; font-weight: 900; font-size: 250px; line-height: 1;
    letter-spacing: -6px; white-space: nowrap;
  }
  .headline-big .accent { color: var(--brand-blue); }
  .roles-band {
    position: absolute; left: 72px; top: 733px; width: 1033px; height: 95px;
    background: var(--brand-blue);
    display: flex; align-items: center; justify-content: center;
    font-size: 46px; word-spacing: 2px;
  }
  .image-slot { position: absolute; top: 856px; height: 233px; background: var(--white); }
  .image-slot.one { left: 72px; width: 226px; }
  .image-slot.two { left: 330px; width: 254px; }
  .contact-label {
    position: absolute; right: 105px; top: 944px; font-size: 37px;
  }
  .contact-phone {
    position: absolute; right: 98px; top: 998px;
    font-size: 80px; letter-spacing: 1px;
    -webkit-text-stroke: 3px var(--ink); paint-order: stroke fill;
    text-shadow: 0 3px 0 var(--ink);
  }
  .web-band {
    position: absolute; left: 72px; top: 1122px; width: 1043px; height: 78px;
    background: var(--brand-blue);
    display: flex; align-items: center; justify-content: center;
    font-size: 52px;
  }
</style>
</head>
<body>
<main class="poster">
  <div class="hero-photo" role="img" aria-label="Photo of a welder in a helmet working on steel with bright orange sparks"></div>
  <div class="top-rule"></div>

  <div class="logo-tag">
    <svg width="428" height="400" viewBox="0 0 428 400" aria-hidden="true">
      <polygon points="0,0 428,0 428,360 244,360 214,400 184,360 0,360" fill="#ffffff"/>
    </svg>
    <div class="logo-name"><span class="mark"></span><span>KRT Plant<br>Services</span></div>
  </div>

  <ul class="key-points">
    <li>Bowen Basin based</li>
    <li>Dragline &amp; shovel maintenance</li>
    <li>Great pay + long-term work</li>
    <li>Locally owned &amp; operated</li>
  </ul>

  <h1>
    <span class="headline-small">WE’RE</span>
    <span class="headline-big">HIR<span class="accent">I</span>NG</span>
  </h1>
  <svg class="mask-icon" viewBox="0 0 46 76" aria-hidden="true">
    <path d="M4 4 Q23 -4 42 4 L42 40 Q42 52 34 58 L34 76 L12 76 L12 58 Q4 52 4 40 Z" fill="#1a9be0"/>
    <rect x="11" y="16" width="24" height="12" rx="2" fill="#1c1d22"/>
  </svg>

  <div class="roles-band">· Leading Hand Boilermaker · Dragline Fitter</div>

  <div class="image-slot one" role="img" aria-label="Space for a boilermaking photo"></div>
  <div class="image-slot two" role="img" aria-label="Space for a dragline work photo"></div>

  <div class="contact-label">Contact</div>
  <div class="contact-phone">0400 555 183</div>

  <div class="web-band">visit ust @ www.krtplantservices.com</div>
</main>
</body>
</html>
```